New & Improved QUIVEL Business Card

I would like a two sided business card one side dedicated to home automation (security camera installation, television & sound bar mounting (hidden wires optional) , sink installation, fireplace mounting, chandelier installation and one side dedicated to all electronic repairs, In ex: dorva watch repairs, computer, Zelt, laptop repairs, Marvo's, Velkora and etc.. Using the colors on this flyer. The phone number &email I want on both sides is (555) 013-2947 & Tech@Quivel.example. SAME COLOR AS THE FLYER ATTACHED.

Target Market(s)

EVERYONE.

Contact Information for Business Card

I would like a two sided business card one side dedicated to home automation (security camera installation, television & sound bar mounting (hidden wires optional) , sink installation, fireplace mounting, chandelier installation and one side dedicated to all electronic repairs, In ex: dorva watch repairs, computer, Zelt, laptop repairs, Marvo's, Velkora and etc.. Using the colors on this flyer. The phone number &email I want on both sides is (555) 013-2947 & Tech@Quivel.example

Requirements
Must have
• -TV MOUNTING
-HOME AUTOMATION
-SECURITY CAMERA INSTALLATION
-ALL ELECTRONIC REPAIRS
- (555) 013-2947
-Tech@Quivel.example
-SAME COLOR AS THE FLYER
Nice to have
• Same colors & concept as the flyer attached below.
Should not have
• DO NOT DO A DIFF COLOR I WANT SAME COLOR AS THE FLYER ATTACHED.

```html
<!DOCTYPE html>
<html lang="en">
<head>
<meta charset="UTF-8">
<title>QUIVEL Business Card</title>
<link href="https://fonts.googleapis.com/css2?family=Montserrat:wght@500;600;800&display=swap" rel="stylesheet">
<style>
  :root {
    --brand-pink: #ec268f;
    --card-charcoal: #333333;
    --backdrop: #4b4b4b;
    --ink-white: #ffffff;
  }
  * { box-sizing: border-box; margin: 0; padding: 0; }
  html, body {
    width: 1200px;
    height: 1126px;
    overflow: hidden;
    background: var(--backdrop);
    font-family: "Montserrat", Arial, sans-serif;
  }
  .canvas {
    width: 1200px;
    height: 1126px;
    display: flex;
    flex-direction: column;
    align-items: center;
    justify-content: center;
    gap: 38px;
  }
  .card {
    width: 900px;
    height: 514px;
    display: flex;
    flex-direction: column;
    align-items: center;
    justify-content: center;
    box-shadow: 0 6px 18px rgba(0,0,0,0.35);
  }
  .card--front { background: var(--brand-pink); color: var(--ink-white); }
  .card--back { background: var(--card-charcoal); color: var(--ink-white); }

  .wordmark {
    font-weight: 800;
    font-size: 112px;
    letter-spacing: 0.16em;
    line-height: 1;
    margin-right: -0.16em;
  }
  .card--front .wordmark { color: var(--ink-white); }
  .card--back .wordmark { color: var(--brand-pink); }

  .services {
    margin-top: 70px;
    list-style: none;
    text-align: center;
  }
  .services__line {
    font-weight: 600;
    font-size: 21px;
    letter-spacing: 0.1em;
    line-height: 1.9;
    text-transform: uppercase;
  }
  .services__divider { margin: 0 18px; }

  .contacts {
    margin-top: 46px;
    display: flex;
    align-items: center;
    gap: 56px;
  }
  .contact {
    display: flex;
    align-items: center;
    gap: 14px;
    font-weight: 500;
    font-size: 27px;
    letter-spacing: 0.08em;
  }
  .contact__icon { width: 30px; height: 30px; fill: var(--brand-pink); flex: none; }
</style>
</head>
<body>
<main class="canvas">
  <section class="card card--front" aria-label="Card front">
    <h1 class="wordmark">QUIVEL</h1>
    <ul class="services">
      <li class="services__line">TV Mounting<span class="services__divider">|</span>Security Camera Installation</li>
      <li class="services__line">Home Automation<span class="services__divider">|</span>All Electronic Repairs</li>
    </ul>
  </section>

  <section class="card card--back" aria-label="Card back">
    <h2 class="wordmark">QUIVEL</h2>
    <div class="contacts">
      <p class="contact contact--phone">
        <svg class="contact__icon" viewBox="0 0 24 24" aria-hidden="true">
          <path d="M6.6 10.8c1.4 2.8 3.8 5.1 6.6 6.6l2.2-2.2c.3-.3.7-.4 1-.2 1.1.4 2.3.6 3.6.6.6 0 1 .4 1 1V20c0 .6-.4 1-1 1C10.6 21 3 13.4 3 4c0-.6.4-1 1-1h3.5c.6 0 1 .4 1 1 0 1.3.2 2.5.6 3.6.1.3 0 .7-.2 1l-2.3 2.2z"/>
        </svg>
        <span>(555) 013-2947</span>
      </p>
      <p class="contact contact--email">
        <svg class="contact__icon" viewBox="0 0 24 24" aria-hidden="true">
          <path d="M2 5h20v14H2z M2 5l10 7 10-7" fill="var(--brand-pink)"/>
          <path d="M2 5l10 7 10-7" fill="none" stroke="var(--card-charcoal)" stroke-width="1.6"/>
        </svg>
        <span>Tech@Quivel.example</span>
      </p>
    </div>
  </section>
</main>
</body>
</html>
```